Website for Brisbeck Current Glide

Require a website for a river float in the City of Edmonton. Located on North Saskatchewan River. Will need to be a coded website with incorporated booking system through Fare Harbor software.

Pages include
Home
Pricing
About
FAQ
Contact

Brisbeck Current Glide is an activity based business that will have customers floating down the North Saskatchewan river in Edmonton AB. The site will have all information needed and a full reservation system. The project was launched to provide people in the Edmonton area a favorite summer activity.

Here are similar websites to reference what our business will be doing and what we are looking for.

mellowbendcanoehire.example
pinegulchloopers.example

Target Market(s)

Families, Groups, Individuals, Anyone who wants to explore the river

Industry/Entity Type

Activities based business/ Outdoor recreational/ River Float

Coding

Coded - Design and coding required

Number of Pages Required

5+ page

Colors
0054AA
0677BA
7BADD7
CADEEF
E8F1F8
F0912C
F2A743
F7CA91
FBE8D2
FDF5EE

```html
<!DOCTYPE html>
<html lang="en">
<head>
<meta charset="utf-8">
<title>Brisbeck Current Glide</title>
<link rel="stylesheet" href="https://fonts.googleapis.com/css2?family=Bowlby+One+SC&family=Courgette&family=Poppins:wght@400;500;600;700&display=swap">
<style>
:root{
  --blue-deep:#0054AA;
  --blue:#0677BA;
  --blue-bright:#1B7FD0;
  --blue-soft:#7BADD7;
  --blue-pale:#CADEEF;
  --blue-mist:#E8F1F8;
  --orange:#F0912C;
  --orange-light:#F2A743;
  --yellow:#F7C92E;
  --page:#ECECF1;
  --ink:#1E1E24;
  --text:#3A3A44;
  --muted:#6B6B75;
  --footer:#232328;
  --white:#FFFFFF;
}
*{box-sizing:border-box;margin:0;padding:0}
html,body{width:1200px;height:4598px;overflow:hidden}
body{background:var(--page);font-family:'Poppins',sans-serif;color:var(--text)}
.page{position:relative;width:1200px;height:4598px;overflow:hidden}
.abs{position:absolute}
.display{font-family:'Bowlby One SC',sans-serif;font-weight:400;color:var(--ink)}
.btn{position:absolute;display:flex;align-items:center;justify-content:center;border-radius:22px;color:var(--white);font-size:12px;font-weight:500;letter-spacing:.5px;text-transform:uppercase}
.btn-blue{background:var(--blue-bright)}
.btn-orange{background:var(--orange)}

/* header */
.site-header{position:absolute;left:0;top:0;width:1200px;height:134px;background:var(--white)}
.nav-link{position:absolute;top:71px;font-size:13px;font-weight:600;color:var(--ink);letter-spacing:.4px}
.nav-link.active{color:var(--blue-deep)}
.brand-disc{position:absolute;left:492px;top:0;width:216px;height:216px;border-radius:50%;background:var(--white)}
.brand-name{position:absolute;left:492px;top:112px;width:216px;text-align:center;font-size:16px;font-weight:700;line-height:19px;color:var(--blue-deep)}
.brand-dot{position:absolute;left:578px;top:50px;width:44px;height:44px;border-radius:50%;background:var(--blue-bright)}

/* hero */
.hero-photo{position:absolute;left:0;top:134px;width:1200px;height:720px;
  background:linear-gradient(180deg,#8d8a82 0%,#b9ad98 22%,#8e8a79 38%,#4f6b3e 52%,#3e5a33 62%,#6f7a72 72%,#55606a 100%)}
.hero-script{position:absolute;left:0;width:1200px;text-align:center;font-family:'Courgette',cursive;color:var(--white)}
.hero-title{position:absolute;left:0;top:484px;width:1200px;text-align:center;font-family:'Bowlby One SC',sans-serif;font-size:34px;color:var(--white);letter-spacing:2px;line-height:40px}
.slider-nav .dot{position:absolute;width:8px;height:8px;border-radius:50%;background:var(--white)}

/* about */
.section-title{position:absolute;left:0;width:1200px;text-align:center;font-size:34px;line-height:40px}
.title-rule{position:absolute;height:3px;width:42px;background:var(--ink)}
.about-copy{position:absolute;left:620px;top:1036px;width:508px}
.about-copy h3{font-size:15px;font-weight:600;color:var(--ink);line-height:27px}
.about-copy p{font-size:12.6px;line-height:15.6px;color:var(--text);margin-top:14px}
.about-copy .hl{color:var(--blue-bright)}
.collage{position:absolute;border:6px solid var(--blue-bright)}

/* pricing */
.pricing{position:absolute;left:0;top:1580px;width:1200px;height:572px;background:var(--blue-bright);overflow:hidden}
.price-badge{position:absolute;left:98px;top:1668px;width:190px;height:108px;background:var(--yellow);transform:rotate(-8deg);border-radius:6px}
.price-amount{position:absolute;left:130px;top:1668px;font-family:'Bowlby One SC',sans-serif;font-size:52px;color:var(--ink);transform:rotate(-8deg);line-height:60px}
.price-unit{position:absolute;left:142px;top:1728px;font-family:'Bowlby One SC',sans-serif;font-size:22px;color:var(--ink);letter-spacing:3px;transform:rotate(-8deg)}
.pricing-intro{position:absolute;left:114px;top:1832px;width:360px;font-size:12.5px;line-height:15.5px;color:var(--white)}
.feature{position:absolute;display:flex;align-items:center;gap:8px;font-size:15px;color:var(--white);font-weight:500;letter-spacing:.3px}
.feature svg{flex:none}

/* faq */
.faq-item{position:absolute;left:614px;width:470px;height:40px;background:var(--white);border:1px solid #dcdde4;display:flex;align-items:center;padding:0 18px;font-size:12.5px;color:var(--ink);letter-spacing:.4px}
.faq-item .chev{position:absolute;right:12px;top:12px}
.faq-open{height:86px;align-items:flex-start;flex-direction:column;padding-top:10px}
.faq-open p{font-size:11.6px;line-height:15px;color:var(--text);margin-top:6px}
.pager{position:absolute;top:2737px;width:32px;height:32px;border:1px solid #c9cad3;background:var(--white);display:flex;align-items:center;justify-content:center;font-size:12px;color:var(--ink)}
.pager.active{background:var(--blue-bright);color:var(--white);border-color:var(--blue-bright)}

/* testimonials */
.testimonials{position:absolute;left:0;top:2883px;width:1200px;height:590px;
  background:linear-gradient(180deg,#3d4856 0%,#56636e 35%,#3f5442 62%,#2c3d31 100%)}
.card{position:absolute;top:3072px;width:295px;height:272px;background:var(--white)}
.quote{position:absolute;top:-14px;left:48px;width:58px;height:58px;border-radius:50%;background:var(--blue-bright);color:var(--white);font-family:'Bowlby One SC',sans-serif;font-size:44px;line-height:78px;text-align:center}
.avatar{position:absolute;left:104px;top:32px;width:86px;height:86px;border-radius:50%;background:linear-gradient(160deg,#f2a743,#c7623a);border:3px solid var(--blue-mist)}
.card-name{position:absolute;left:0;top:124px;width:295px;text-align:center;font-size:16px;color:var(--ink)}
.card-role{position:absolute;left:0;top:146px;width:295px;text-align:center;font-size:13px;color:var(--blue-bright)}
.card-text{position:absolute;left:20px;top:172px;width:255px;text-align:center;font-size:11.3px;line-height:14px;color:var(--text)}
.stars{position:absolute;left:0;top:228px;width:295px;text-align:center;font-size:12px;color:var(--orange);letter-spacing:3px}
.t-dot{position:absolute;top:3390px;width:6px;height:6px;border-radius:50%;background:var(--blue-pale)}

/* follow */
.tile{position:absolute;top:3634px;width:195px;height:193px}

/* subscribe */
.email-input{position:absolute;left:327px;top:3997px;width:384px;height:38px;border-radius:20px;background:var(--white);border:1px solid #d6d7de;font-size:12px;color:var(--muted);display:flex;align-items:center;padding-left:22px}

/* footer */
.footer{position:absolute;left:0;top:4186px;width:1200px;height:357px;background:var(--footer)}
.foot-head{position:absolute;top:4303px;font-family:'Bowlby One SC',sans-serif;font-size:15px;color:var(--white);letter-spacing:1px}
.foot-link{position:absolute;left:423px;font-size:12.5px;color:var(--white)}
.foot-link span{margin-right:16px}
.foot-line{position:absolute;left:660px;font-size:12px;color:var(--white)}
.copyright{position:absolute;left:111px;top:4558px;font-size:11.5px;color:var(--ink)}
.copyright b{color:var(--blue-deep);font-weight:500}
.social{position:absolute;top:4552px;width:30px;height:30px;border-radius:50%;background:var(--blue-deep)}
</style>
</head>
<body>
<div class="page">

  <!-- hero -->
  <div class="hero-photo" role="img" aria-label="Photo of the downtown Edmonton skyline above the North Saskatchewan river with a bridge and a raft on the water"></div>
  <div class="slider-nav">
    <span class="dot" style="left:70px;top:446px"></span>
    <span class="abs" style="left:66px;top:463px;width:34px;height:2px;background:var(--white)"></span>
    <span class="abs" style="left:104px;top:456px;font-size:11px;color:var(--white);font-style:italic">02</span>
    <span class="dot" style="left:70px;top:476px"></span>
    <span class="dot" style="left:70px;top:492px"></span>
  </div>
  <div class="hero-script" style="top:452px;font-size:28px">Float the</div>
  <div class="hero-title">North Saskatchewan</div>
  <div class="hero-script" style="top:522px;font-size:24px">Through Downtown Edmonton</div>
  <div class="btn btn-blue" style="left:568px;top:571px;width:156px;height:36px">Book Now</div>

  <svg class="abs" style="left:0;top:680px" width="1200" height="180" viewBox="0 0 1200 180" aria-hidden="true">
    <path d="M0 50 C220 70 420 150 600 130 C780 110 900 20 1200 30 L1200 180 L0 180 Z" fill="var(--blue-bright)"/>
    <path d="M0 80 C200 95 380 170 580 160 C790 150 940 60 1200 70 L1200 180 L0 180 Z" fill="var(--blue-deep)" opacity=".9"/>
    <path d="M0 100 C230 115 400 180 600 176 C800 172 960 80 1200 90 L1200 180 L0 180 Z" fill="var(--page)"/>
  </svg>

  <!-- header -->
  <header class="site-header">
    <a class="nav-link active" style="left:112px">HOME</a>
    <a class="nav-link" style="left:209px">PRICING</a>
    <a class="nav-link" style="left:323px">ABOUT US</a>
    <a class="nav-link" style="left:754px">FAQ</a>
    <a class="nav-link" style="left:830px">CONTACT</a>
    <div class="btn btn-blue" style="left:964px;top:57px;width:158px;height:41px;justify-content:flex-start;padding-left:22px;gap:14px;font-size:11.5px">Book Now
      <svg width="42" height="10" viewBox="0 0 42 10"><path d="M0 5H40M34 1L40 5L34 9" stroke="#fff" stroke-width="1.6" fill="none"/></svg>
    </div>
  </header>
  <div class="brand-disc"></div>
  <div class="brand-dot"></div>
  <div class="brand-name">Brisbeck<br>Current Glide</div>

  <!-- about -->
  <h2 class="section-title display" style="top:930px">About Us</h2>
  <div class="title-rule" style="left:579px;top:978px"></div>

  <div class="collage" role="img" aria-label="Photo of a yellow raft crew paddling through whitewater"
       style="left:76px;top:1000px;width:500px;height:282px;border-radius:48% 52% 40% 60% / 60% 50% 50% 40%;border-width:0 6px 0 0;background:linear-gradient(150deg,#7c8a93,#e5d35a 45%,#c9d3d8 70%,#5b6d76)"></div>
  <div class="collage" role="img" aria-label="Photo of a kayaker on calm water"
       style="left:96px;top:1238px;width:166px;height:152px;border-radius:50%;background:linear-gradient(160deg,#3f6a8a,#d07a32 55%,#27455c)"></div>
  <div class="collage" role="img" aria-label="Photo of a kayaker in a yellow boat on rapids"
       style="left:238px;top:1254px;width:166px;height:204px;border-radius:50%;border-color:#4a7a2e;background:linear-gradient(160deg,#5c6b6e,#d9c443 60%,#4b5a5a)"></div>
  <div class="collage" role="img" aria-label="Photo of the white shuttle bus"
       style="left:396px;top:1252px;width:176px;height:176px;border-radius:50%;border-color:var(--orange);background:linear-gradient(160deg,#f4c48d,#e9e5e0 55%,#c79a63)"></div>

  <div class="about-copy">
    <h3>Float the North Saskatchewan through downtown Edmonton<br>Edmonton's Best Summer Activity</h3>
    <p>We provide the <span class="hl">lifejacket, paddle, river tube and shuttle</span> service.<br>You just have to show up.</p>
    <p>Brisbeck Current Glide was launched to provide people in the Edmonton area a favorite summer activity. Nothing is better on a hot summer day, than spending it on the river and seeing Edmonton from a new perspective. Our home base and meeting spot is at Heronbank Landing (Map Link), by the Glasshouse Gardens. This is where you will check in, and board the shuttle. The shuttle will take all floaters up river to Aspen Park Boat Launch. Once there, your tube will be waiting. Once on the river, you can sit back, relax, explore and enjoy the view. Once you complete the float, and arrive back at Heronbank Landing, staff will be available to assist in exiting the river where you will return your tube and gear. Safety is our top priority, but having fun is a close second.</p>
    <p>Don't miss out on Edmonton's best summer activity.</p>
  </div>
  <div class="btn btn-blue" style="left:625px;top:1378px;width:154px;height:37px">Book Now</div>

  <!-- pricing -->
  <section class="pricing">
    <svg class="abs" style="left:0;top:0" width="1200" height="572" viewBox="0 0 1200 572" role="img" aria-label="Photo of a smiling crew in helmets paddling a blue raft through whitewater">
      <defs>
        <linearGradient id="raftPhoto" x1="0" y1="0" x2="1" y2="1">
          <stop offset="0" stop-color="#8a6a3e"/>
          <stop offset=".4" stop-color="#a88d5e"/>
          <stop offset=".65" stop-color="#3f6fb0"/>
          <stop offset="1" stop-color="#d9e3ea"/>
        </linearGradient>
      </defs>
      <path d="M410 0 C390 70 470 110 560 130 C640 150 600 250 560 300 C520 350 470 400 520 470 C560 530 660 560 720 572 L1200 572 L1200 0 Z" fill="url(#raftPhoto)"/>
    </svg>
    <div class="abs display" style="left:0;top:64px;width:1200px;text-align:center;font-size:32px;color:var(--white)">Pricing</div>
    <div class="abs" style="left:566px;top:110px;width:66px;height:3px;background:var(--white)"></div>
  </section>

  <div class="price-badge"></div>
  <div class="price-amount">$30/</div>
  <div class="price-unit">PERSON</div>
  <p class="pricing-intro">We keep our pricing simple and include everything you need:Premium comfort float tube with backrest and cup holder</p>

  <div class="feature" style="left:114px;top:1902px"><svg width="20" height="20" viewBox="0 0 20 20"><circle cx="10" cy="10" r="8.5" stroke="#fff" stroke-width="1.6" fill="none"/><path d="M6 10.5L9 13L14.5 7" stroke="#fff" stroke-width="1.8" fill="none"/></svg>Lifejacket</div>
  <div class="feature" style="left:243px;top:1902px"><svg width="20" height="20" viewBox="0 0 20 20"><circle cx="10" cy="10" r="8.5" stroke="#fff" stroke-width="1.6" fill="none"/><path d="M6 10.5L9 13L14.5 7" stroke="#fff" stroke-width="1.8" fill="none"/></svg>Paddle</div>
  <div class="feature" style="left:350px;top:1902px"><svg width="20" height="20" viewBox="0 0 20 20"><circle cx="10" cy="10" r="8.5" stroke="#fff" stroke-width="1.6" fill="none"/><path d="M6 10.5L9 13L14.5 7" stroke="#fff" stroke-width="1.8" fill="none"/></svg>Safety Training</div>
  <div class="feature" style="left:114px;top:1936px"><svg width="20" height="20" viewBox="0 0 20 20"><circle cx="10" cy="10" r="8.5" stroke="#fff" stroke-width="1.6" fill="none"/><path d="M6 10.5L9 13L14.5 7" stroke="#fff" stroke-width="1.8" fill="none"/></svg>Round Trip Shuttle Service</div>
  <div class="feature" style="left:357px;top:1936px"><svg width="20" height="20" viewBox="0 0 20 20"><circle cx="10" cy="10" r="8.5" stroke="#fff" stroke-width="1.6" fill="none"/><path d="M6 10.5L9 13L14.5 7" stroke="#fff" stroke-width="1.8" fill="none"/></svg>Parking</div>
  <div class="feature" style="left:114px;top:1973px"><svg width="20" height="20" viewBox="0 0 20 20"><circle cx="10" cy="10" r="8.5" stroke="#fff" stroke-width="1.6" fill="none"/><path d="M6 10.5L9 13L14.5 7" stroke="#fff" stroke-width="1.8" fill="none"/></svg>Staff Assistance</div>
  <div class="feature" style="left:284px;top:1973px"><svg width="20" height="20" viewBox="0 0 20 20"><circle cx="10" cy="10" r="8.5" stroke="#fff" stroke-width="1.6" fill="none"/><path d="M6 10.5L9 13L14.5 7" stroke="#fff" stroke-width="1.8" fill="none"/></svg>Unlimited Fun!</div>
  <div class="btn btn-orange" style="left:114px;top:2032px;width:154px;height:37px">Book Now</div>

  <!-- faq -->
  <svg class="abs" style="left:56px;top:2284px" width="545" height="486" viewBox="0 0 545 486" role="img" aria-label="Photo of a father and child in a yellow kayak holding a paddle">
    <defs>
      <linearGradient id="kayakPhoto" x1="0" y1="0" x2="1" y2="1">
        <stop offset="0" stop-color="#9aa3a8"/>
        <stop offset=".45" stop-color="#6f7e86"/>
        <stop offset=".7" stop-color="#e6cd3a"/>
        <stop offset="1" stop-color="#3c4a50"/>
      </linearGradient>
    </defs>
    <path d="M20 170 C60 70 200 70 300 40 C400 10 470 0 520 40 C545 150 540 300 500 420 C470 480 360 490 260 470 C150 450 30 420 10 330 C0 260 5 210 20 170 Z" fill="var(--blue-bright)"/>
    <path d="M4 190 C40 100 180 100 290 70 C390 40 460 30 530 60 L540 300 C530 380 470 440 380 460 C270 480 130 460 40 400 C0 360 -6 260 4 190 Z" fill="url(#kayakPhoto)"/>
  </svg>

  <h2 class="abs display" style="left:630px;top:2252px;font-size:34px">FAQ</h2>
  <div class="title-rule" style="left:632px;top:2300px;width:38px"></div>

  <div class="faq-item faq-open" style="top:2343px">
    How do I reserve my float?
    <p>We highly recommend booking online, as we do sell out. BOOK NOW Floats can also be reserved on-site at Heronbank Landing, on a first come first serve basis.</p>
    <svg class="chev" width="16" height="16" viewBox="0 0 16 16"><circle cx="8" cy="8" r="8" fill="var(--blue-bright)"/><path d="M5 6.5L8 9.5L11 6.5" stroke="#fff" stroke-width="1.5" fill="none"/></svg>
  </div>
  <div class="faq-item" style="top:2442px">What safety information should I know?<svg class="chev" width="16" height="16" viewBox="0 0 16 16"><circle cx="8" cy="8" r="8" fill="var(--blue-bright)"/><path d="M9.5 5L6.5 8L9.5 11" stroke="#fff" stroke-width="1.5" fill="none"/></svg></div>
  <div class="faq-item" style="top:2489px">What is included?<svg class="chev" width="16" height="16" viewBox="0 0 16 16"><circle cx="8" cy="8" r="8" fill="var(--blue-bright)"/><path d="M9.5 5L6.5 8L9.5 11" stroke="#fff" stroke-width="1.5" fill="none"/></svg></div>
  <div class="faq-item" style="top:2536px">What should I bring?<svg class="chev" width="16" height="16" viewBox="0 0 16 16"><circle cx="8" cy="8" r="8" fill="var(--blue-bright)"/><path d="M9.5 5L6.5 8L9.5 11" stroke="#fff" stroke-width="1.5" fill="none"/></svg></div>
  <div class="faq-item" style="top:2582px">Where are you located?<svg class="chev" width="16" height="16" viewBox="0 0 16 16"><circle cx="8" cy="8" r="8" fill="var(--blue-bright)"/><path d="M9.5 5L6.5 8L9.5 11" stroke="#fff" stroke-width="1.5" fill="none"/></svg></div>
  <div class="faq-item" style="top:2629px">What time should I arrive?<svg class="chev" width="16" height="16" viewBox="0 0 16 16"><circle cx="8" cy="8" r="8" fill="var(--blue-bright)"/><path d="M9.5 5L6.5 8L9.5 11" stroke="#fff" stroke-width="1.5" fill="none"/></svg></div>
  <div class="faq-item" style="top:2675px">Where should I park?<svg class="chev" width="16" height="16" viewBox="0 0 16 16"><circle cx="8" cy="8" r="8" fill="var(--blue-bright)"/><path d="M9.5 5L6.5 8L9.5 11" stroke="#fff" stroke-width="1.5" fill="none"/></svg></div>

  <div class="pager active" style="left:620px">1</div>
  <div class="pager" style="left:664px">2</div>
  <div class="pager" style="left:709px">3</div>
  <div class="pager" style="left:754px">4</div>
  <div class="pager" style="left:798px">&gt;&gt;</div>

  <!-- testimonials -->
  <section class="testimonials" role="img" aria-label="Dim photo of the Edmonton skyline and river valley trees"></section>
  <h2 class="section-title display" style="top:2944px;color:var(--white)">Testimonials</h2>
  <div class="abs" style="left:0;top:2990px;width:1200px;text-align:center;font-size:14px;color:var(--white)">What Clients say about us</div>

  <article class="card" style="left:113px">
    <div class="quote">“</div>
    <div class="avatar" role="img" aria-label="Portrait of the client"></div>
    <div class="card-name">Dorian Vale</div>
    <div class="card-role">Creative Director</div>
    <p class="card-text">Lorem Ipsum simply dummy text printing and typesetting industry simply dummy a psum is simply dummy</p>
    <div class="stars">★★★★★</div>
  </article>
  <article class="card" style="left:451px">
    <div class="quote">“</div>
    <div class="avatar" role="img" aria-label="Portrait of the client"></div>
    <div class="card-name">Maren Holt</div>
    <div class="card-role">Director</div>
    <p class="card-text">Lorem Ipsum simply dummy text printing and typesetting industry simply dummy a psum is simply dummy</p>
    <div class="stars">★★★★★</div>
  </article>
  <article class="card" style="left:791px">
    <div class="quote">“</div>
    <div class="avatar" role="img" aria-label="Portrait of the client"></div>
    <div class="card-name">Talia Brook</div>
    <div class="card-role">Creative Director</div>
    <p class="card-text">Lorem Ipsum simply dummy text printing and typesetting industry simply dummy a psum is simply dummy</p>
    <div class="stars">★★★★★</div>
  </article>
  <span class="t-dot" style="left:440px"></span>
  <span class="t-dot" style="left:583px;background:var(--blue-bright)"></span>
  <span class="t-dot" style="left:596px"></span>
  <span class="t-dot" style="left:609px"></span>

  <!-- follow -->
  <h2 class="section-title display" style="top:3542px;font-size:32px">Follow Us On</h2>
  <div class="abs" style="left:0;top:3587px;width:1200px;text-align:center;font-size:14px;font-weight:600;color:var(--blue-bright)">info@brisbeckcurrentglide.example</div>
  <div class="tile" style="left:73px;background:linear-gradient(160deg,#5f8fa9,#e6cf3b 55%,#2d5f86)" role="img" aria-label="Photo of rafters in whitewater"></div>
  <div class="tile" style="left:288px;background:linear-gradient(160deg,#c9c6b8,#e2c73a 50%,#8b2b2b)" role="img" aria-label="Photo of rafters in red life jackets paddling"></div>
  <div class="tile" style="left:502px;background:linear-gradient(160deg,#2a2a33,#3b3b46 55%,#55503a)" role="img" aria-label="Darkened photo of a raft on the river"></div>
  <div class="tile" style="left:716px;background:linear-gradient(180deg,#c5cdd6,#9fa9a7 45%,#567a4a 70%,#3f6b7a)" role="img" aria-label="Photo of the river winding past the city skyline"></div>
  <div class="tile" style="left:929px;background:linear-gradient(160deg,#d8d0c4,#e2c140 45%,#c83a37 80%)" role="img" aria-label="Photo of a crew in a red raft"></div>

  <!-- subscribe -->
  <h2 class="section-title display" style="top:3913px;font-size:32px">Subscribe To Our Newsletter</h2>
  <div class="abs" style="left:0;top:3958px;width:1200px;text-align:center;font-size:13px;color:var(--text)">To Receive The latest News And Update</div>
  <div class="email-input">Your E-Mail</div>
  <div class="btn btn-blue" style="left:729px;top:3997px;width:152px;height:38px;font-weight:600">Submit</div>

  <!-- footer -->
  <svg class="abs" style="left:0;top:4090px" width="1200" height="110" viewBox="0 0 1200 110" aria-hidden="true">
    <path d="M0 20 C200 10 380 60 560 80 C760 100 940 10 1200 0 L1200 110 L0 110 Z" fill="var(--blue-bright)"/>
    <path d="M0 50 C220 40 400 90 600 100 C800 108 960 40 1200 30 L1200 110 L0 110 Z" fill="var(--footer)"/>
  </svg>
  <footer class="footer"></footer>

  <div class="abs" style="left:120px;top:4300px;width:36px;height:36px;border-radius:50%;background:var(--blue-bright)"></div>
  <div class="abs" style="left:100px;top:4346px;width:190px;font-size:17px;font-weight:700;line-height:21px;color:var(--white)">Brisbeck<br>Current Glide</div>
  <div class="abs" style="left:102px;top:4473px;font-family:'Bowlby One SC',sans-serif;font-size:12.5px;color:var(--white);letter-spacing:.6px">Floating 7 Days A Week</div>

  <div class="foot-head" style="left:423px">Quick Link</div>
  <div class="abs" style="left:423px;top:4326px;width:36px;height:2px;background:var(--white)"></div>
  <div class="foot-link" style="top:4343px"><span>&gt;</span>HOME</div>
  <div class="foot-link" style="top:4370px"><span>&gt;</span>PRICING</div>
  <div class="foot-link" style="top:4397px"><span>&gt;</span>ABOUT</div>
  <div class="foot-link" style="top:4424px"><span>&gt;</span>FAQ</div>
  <div class="foot-link" style="top:4451px"><span>&gt;</span>CONTACT</div>

  <div class="foot-head" style="left:629px">Contact Info</div>
  <div class="abs" style="left:629px;top:4326px;width:36px;height:2px;background:var(--white)"></div>
  <svg class="abs" style="left:629px;top:4348px" width="14" height="18" viewBox="0 0 14 18"><path d="M7 1C3.7 1 1 3.6 1 6.8C1 11 7 17 7 17S13 11 13 6.8C13 3.6 10.3 1 7 1Z" fill="none" stroke="#fff" stroke-width="1.6"/><circle cx="7" cy="7" r="2.2" fill="#fff"/></svg>
  <div class="foot-line" style="top:4348px">4410 Willowmere Rd NW,</div>
  <div class="foot-line" style="top:4371px">Edmonton, AB</div>
  <svg class="abs" style="left:629px;top:4418px" width="16" height="12" viewBox="0 0 16 12"><rect x="0.8" y="0.8" width="14.4" height="10.4" fill="#fff"/><path d="M1 1.2L8 6.5L15 1.2" stroke="var(--footer)" stroke-width="1.3" fill="none"/></svg>
  <div class="foot-line" style="top:4416px">0064 555010427</div>
  <svg class="abs" style="left:630px;top:4439px" width="14" height="14" viewBox="0 0 14 14"><path d="M3 1L5.5 3.8L4.2 5.6C5 7.4 6.6 9 8.4 9.8L10.2 8.5L13 11L11.4 13C6 12.6 1.4 8 1 2.6Z" fill="#fff"/></svg>
  <div class="foot-line" style="top:4439px">780 555 0199</div>

  <div class="foot-head" style="left:862px;top:4285px">Map</div>
  <div class="abs" style="left:866px;top:4327px;width:262px;height:135px;background:linear-gradient(135deg,#e6e8ea,#d3dbe0 60%,#e9ece6)" role="img" aria-label="Street map of the meeting point"></div>

  <div class="copyright">Copyright © 2022 <b>BRISBECK CURRENT GLIDE</b>. All Rights Reserved.</div>
  <span class="social" style="left:977px" aria-label="Social link"></span>
  <span class="social" style="left:1017px" aria-label="Social link"></span>
  <span class="social" style="left:1056px" aria-label="Social link"></span>
  <span class="social" style="left:1096px" aria-label="Social link"></span>

</div>
</body>
</html>
```